Outlast the Coming Storm - book cover

A book cover (front) to be used on print book. Book will be 5 inches by 8 inches. Also need the cover image (as jpg) for promotional purposes. Include company logo on cover - I've included a couple of versions. Include my name as author: Dr. Corliss Vandemeer

Title of book is:
Weathering Every Market Tide
(sub-title) through coaching clear reasoning

this can be a sub-sub title, or a call out or "burst" standing alone -
A survival guide for 21st century business

If you'd like some inspiration, check out my web page: www.mentorvale.com
The company colors are red, white and blue, but I think red might be too harsh - use with caution if you use it.
RGB values of the company are:
Blue: 0/66/105
Red: 190/30/45

Target Market(s)

Business / Professionals / Chief Executives of Companies with more than 1000 employees

Industry/Entity Type

Business

Font styles to use
Serif

Colors
0255a3
ffffff

Requirements
Must have
• The title should make them pause and say "I need to get this book if I want my company to survive another 20 years!"
Nice to have
• Some image that signifies the future and / or uncertainty. Should be abstract - not people, not technology (which could change and then make the book look old). If you'd like to make the design a wrap from front to back, that is fine. I am not sure what text will go on the back at this point, so I may have to come back to you in a few months for an update.

```html
<!DOCTYPE html>
<html lang="en">
<head>
<meta charset="utf-8">
<title>Weathering Every Market Tide – Book Cover</title>
<link href="https://fonts.googleapis.com/css2?family=Arimo:wght@400;700&family=Roboto+Condensed:wght@700&display=swap" rel="stylesheet">
<style>
  :root {
    --backdrop: #e4e7e6;
    --cover-white: #ffffff;
    --brand-blue: #0255a3;
    --band-blue: #3d7cc3;
    --title-blue: #2f78c4;
    --ink-grey: #3a3f44;
    --frost-light: #f3f6fa;
    --frost-mid: #dfe7f0;
    --frost-deep: #c9d6e4;
  }
  * { box-sizing: border-box; margin: 0; padding: 0; }
  html, body {
    width: 1200px; height: 800px; overflow: hidden;
    background: var(--backdrop);
  }
  .stage {
    width: 1200px; height: 800px;
    display: flex; align-items: center; justify-content: center;
  }
  .cover {
    position: relative;
    width: 460px; height: 736px;
    background: var(--cover-white);
    overflow: hidden;
    font-family: "Arimo", Arial, sans-serif;
  }
  .cover-frost {
    position: absolute; left: 0; top: 150px; width: 100%; height: 586px;
    background:
      radial-gradient(ellipse at 55% 35%, var(--frost-mid) 0%, transparent 55%),
      linear-gradient(180deg, var(--cover-white) 0%, var(--frost-light) 30%, var(--frost-mid) 70%, var(--frost-deep) 100%);
  }
  .tagline-band {
    position: relative;
    height: 40px;
    background: var(--band-blue);
    color: var(--cover-white);
    font-size: 17px;
    letter-spacing: 0.5px;
    display: flex; align-items: center; justify-content: center;
  }
  .publisher-mark {
    position: relative;
    margin-top: 52px;
    text-align: center;
    font-size: 19px;
    font-weight: 700;
    color: var(--brand-blue);
  }
  .title-block {
    position: relative;
    margin-top: 92px;
    padding-left: 24px;
  }
  .title-main {
    font-size: 60px;
    font-weight: 400;
    color: var(--title-blue);
    line-height: 1;
  }
  .title-line {
    margin-top: 8px;
    font-size: 23px;
    letter-spacing: 3px;
    color: var(--ink-grey);
  }
  .subtitle {
    margin-top: 6px;
    font-size: 20px;
    color: var(--title-blue);
  }
  .author {
    position: absolute;
    left: 24px; bottom: 46px;
    font-family: "Roboto Condensed", "Arial Narrow", sans-serif;
    font-weight: 700;
    font-size: 44px;
    color: var(--brand-blue);
  }
</style>
</head>
<body>
<main class="stage">
  <article class="cover">
    <div class="cover-frost" role="img" aria-label="Abstract frosted glass with rain droplets"></div>
    <header class="tagline-band">A survival guide for 21st century business</header>
    <p class="publisher-mark">MentorVale</p>
    <section class="title-block">
      <h1 class="title-main">Weathering</h1>
      <p class="title-line">EVERY MARKET TIDE</p>
      <p class="subtitle">through coaching clear reasoning</p>
    </section>
    <p class="author">Dr. Corliss Vandemeer</p>
  </article>
</main>
</body>
</html>
```